Copper Lantern LLC Business Card

We need a business card design for a newco in Texas. We are a team of professionals who join start ups as founders and help launch their businesses, which are primarily related to food and beverage and the service side of the industry. We love local and craft and are partners in businesses in the local meat, BBQ and Burger, fine dining, and beverage alcohol businesses. Our specialty is finance and the business side of start ups, including assisting with capital raises as principals, not brokers. We do not currently have any logos or graphics for this entity. Our values include helping people succeed, rooting for the underdog, healthy food, the environment and being good citizens.

Target Market(s)

Everybody but also Angel Investors, CPAs, Bankers, Entrepreneurs

Industry/Entity Type

Business

Contact Information for Business Card

Fields for Business Name, Title, Email Address, Phone Number. Place to add mailing address and web domain later.

Font styles to use
Sans Serif

Colors

Designer to choose colors to be used in the design.

Requirements
Should not have
• Pictures of booze bottles or drinks thought there could be a social scene that does not strictly focus on those. No cows, cowboy hats or ranches. We are not a Wall Street type entity so no huge office buildings or skylines.

```html
<!DOCTYPE html>
<html lang="en">
<head>
<meta charset="utf-8">
<title>Copper Lantern LLC – Business Card Colourways</title>
<link rel="stylesheet" href="https://fonts.googleapis.com/css2?family=Ubuntu:wght@300;400;500;700&display=swap">
<style>
  :root {
    --backdrop: #b2b3b2;
    --card: #ffffff;
    --ink: #333333;
    --ink-soft: #444444;
    --lime: #b0cb1f;
    --sky: #009ee0;
    --magenta: #e2097f;
    --scarlet: #e32124;
  }
  * { box-sizing: border-box; margin: 0; padding: 0; }
  html, body {
    width: 1200px;
    height: 2635px;
    overflow: hidden;
    background: var(--backdrop);
    font-family: "Ubuntu", Arial, sans-serif;
    color: var(--ink);
  }
  .sheet { position: relative; width: 1200px; height: 2635px; }

  .card {
    position: absolute;
    left: 121px;
    width: 958px;
    height: 548px;
    background: var(--card);
  }
  .card--lime    { top: 141px;  --accent: var(--lime); }
  .card--sky     { top: 748px;  --accent: var(--sky); }
  .card--magenta { top: 1344px; --accent: var(--magenta); }
  .card--scarlet { top: 1944px; --accent: var(--scarlet); }

  .brand {
    position: absolute;
    left: 45px;
    top: 68px;
    width: 390px;
    height: 388px;
    display: flex;
    align-items: center;
    gap: 22px;
  }
  .brand__dot {
    flex: 0 0 auto;
    width: 64px;
    height: 64px;
    border-radius: 50%;
    background: var(--accent);
  }
  .brand__name {
    font-weight: 700;
    font-size: 50px;
    line-height: 1.05;
    color: var(--accent);
  }

  .holder {
    position: absolute;
    left: 525px;
    top: 50px;
  }
  .holder__name {
    font-weight: 300;
    font-size: 39px;
    line-height: 46px;
    color: var(--ink);
  }
  .holder__name em {
    font-style: normal;
    font-weight: 400;
    color: var(--accent);
  }
  .holder__title {
    margin-top: 6px;
    font-weight: 300;
    font-size: 27px;
    line-height: 32px;
    color: var(--ink-soft);
  }

  .contact {
    position: absolute;
    left: 480px;
    top: 232px;
    list-style: none;
  }
  .contact__company {
    padding-left: 61px;
    font-weight: 400;
    font-size: 31px;
    line-height: 40px;
    color: var(--accent);
  }
  .contact__row {
    display: flex;
    align-items: flex-start;
  }
  .contact__icon {
    flex: 0 0 61px;
    height: 39px;
    display: flex;
    align-items: center;
    padding-left: 10px;
  }
  .contact__icon svg {
    width: 24px;
    height: 24px;
    fill: none;
    stroke: var(--ink);
    stroke-width: 1.6;
    stroke-linecap: round;
    stroke-linejoin: round;
  }
  .contact__text {
    font-weight: 300;
    font-size: 30px;
    line-height: 39px;
    color: var(--ink);
  }
</style>
</head>
<body>
<main class="sheet">

  <section class="card card--lime">
    <div class="brand"><span class="brand__dot"></span><span class="brand__name">Copper<br>Lantern<br>LLC</span></div>
    <div class="holder"><p class="holder__name">Yuorown <em>Fullname</em></p><p class="holder__title">Job Title / Occuoation</p></div>
    <ul class="contact">
      <li class="contact__company">COPPER LANTERN LLC</li>
      <li class="contact__row"><span class="contact__icon"><svg viewBox="0 0 24 24"><path d="M12 22s-7-7.5-7-12.5a7 7 0 0 1 14 0C19 14.5 12 22 12 22z"/><circle cx="12" cy="9.5" r="2.5"/></svg></span><span class="contact__text">Suite A1, 111 Your Street<br>Yourowncity, TX 99999</span></li>
      <li class="contact__row"><span class="contact__icon"><svg viewBox="0 0 24 24"><path d="M5 3h4l2 5-2.5 1.5a11 11 0 0 0 6 6L16 13l5 2v4a2 2 0 0 1-2 2A16 16 0 0 1 3 5a2 2 0 0 1 2-2z"/></svg></span><span class="contact__text">915 555 5555<br>915 555 5555</span></li>
      <li class="contact__row"><span class="contact__icon"><svg viewBox="0 0 24 24"><rect x="3" y="6" width="18" height="12"/><path d="M3 6l9 7 9-7"/></svg></span><span class="contact__text">your.email@yoursite.com</span></li>
      <li class="contact__row"><span class="contact__icon"><svg viewBox="0 0 24 24"><circle cx="12" cy="12" r="9"/><path d="M3 12h18M12 3c3 3 3 15 0 18M12 3c-3 3-3 15 0 18"/></svg></span><span class="contact__text">www.yoursite.com</span></li>
    </ul>
  </section>

  <section class="card card--sky">
    <div class="brand"><span class="brand__dot"></span><span class="brand__name">Copper<br>Lantern<br>LLC</span></div>
    <div class="holder"><p class="holder__name">Yuorown <em>Fullname</em></p><p class="holder__title">Job Title / Occuoation</p></div>
    <ul class="contact">
      <li class="contact__company">COPPER LANTERN LLC</li>
      <li class="contact__row"><span class="contact__icon"><svg viewBox="0 0 24 24"><path d="M12 22s-7-7.5-7-12.5a7 7 0 0 1 14 0C19 14.5 12 22 12 22z"/><circle cx="12" cy="9.5" r="2.5"/></svg></span><span class="contact__text">Suite A1, 111 Your Street<br>Yourowncity, TX 99999</span></li>
      <li class="contact__row"><span class="contact__icon"><svg viewBox="0 0 24 24"><path d="M5 3h4l2 5-2.5 1.5a11 11 0 0 0 6 6L16 13l5 2v4a2 2 0 0 1-2 2A16 16 0 0 1 3 5a2 2 0 0 1 2-2z"/></svg></span><span class="contact__text">915 555 5555<br>915 555 5555</span></li>
      <li class="contact__row"><span class="contact__icon"><svg viewBox="0 0 24 24"><rect x="3" y="6" width="18" height="12"/><path d="M3 6l9 7 9-7"/></svg></span><span class="contact__text">your.email@yoursite.com</span></li>
      <li class="contact__row"><span class="contact__icon"><svg viewBox="0 0 24 24"><circle cx="12" cy="12" r="9"/><path d="M3 12h18M12 3c3 3 3 15 0 18M12 3c-3 3-3 15 0 18"/></svg></span><span class="contact__text">www.yoursite.com</span></li>
    </ul>
  </section>

  <section class="card card--magenta">
    <div class="brand"><span class="brand__dot"></span><span class="brand__name">Copper<br>Lantern<br>LLC</span></div>
    <div class="holder"><p class="holder__name">Yuorown <em>Fullname</em></p><p class="holder__title">Job Title / Occuoation</p></div>
    <ul class="contact">
      <li class="contact__company">COPPER LANTERN LLC</li>
      <li class="contact__row"><span class="contact__icon"><svg viewBox="0 0 24 24"><path d="M12 22s-7-7.5-7-12.5a7 7 0 0 1 14 0C19 14.5 12 22 12 22z"/><circle cx="12" cy="9.5" r="2.5"/></svg></span><span class="contact__text">Suite A1, 111 Your Street<br>Yourowncity, TX 99999</span></li>
      <li class="contact__row"><span class="contact__icon"><svg viewBox="0 0 24 24"><path d="M5 3h4l2 5-2.5 1.5a11 11 0 0 0 6 6L16 13l5 2v4a2 2 0 0 1-2 2A16 16 0 0 1 3 5a2 2 0 0 1 2-2z"/></svg></span><span class="contact__text">915 555 5555<br>915 555 5555</span></li>
      <li class="contact__row"><span class="contact__icon"><svg viewBox="0 0 24 24"><rect x="3" y="6" width="18" height="12"/><path d="M3 6l9 7 9-7"/></svg></span><span class="contact__text">your.email@yoursite.com</span></li>
      <li class="contact__row"><span class="contact__icon"><svg viewBox="0 0 24 24"><circle cx="12" cy="12" r="9"/><path d="M3 12h18M12 3c3 3 3 15 0 18M12 3c-3 3-3 15 0 18"/></svg></span><span class="contact__text">www.yoursite.com</span></li>
    </ul>
  </section>

  <section class="card card--scarlet">
    <div class="brand"><span class="brand__dot"></span><span class="brand__name">Copper<br>Lantern<br>LLC</span></div>
    <div class="holder"><p class="holder__name">Yuorown <em>Fullname</em></p><p class="holder__title">Job Title / Occuoation</p></div>
    <ul class="contact">
      <li class="contact__company">COPPER LANTERN LLC</li>
      <li class="contact__row"><span class="contact__icon"><svg viewBox="0 0 24 24"><path d="M12 22s-7-7.5-7-12.5a7 7 0 0 1 14 0C19 14.5 12 22 12 22z"/><circle cx="12" cy="9.5" r="2.5"/></svg></span><span class="contact__text">Suite A1, 111 Your Street<br>Yourowncity, TX 99999</span></li>
      <li class="contact__row"><span class="contact__icon"><svg viewBox="0 0 24 24"><path d="M5 3h4l2 5-2.5 1.5a11 11 0 0 0 6 6L16 13l5 2v4a2 2 0 0 1-2 2A16 16 0 0 1 3 5a2 2 0 0 1 2-2z"/></svg></span><span class="contact__text">915 555 5555<br>915 555 5555</span></li>
      <li class="contact__row"><span class="contact__icon"><svg viewBox="0 0 24 24"><rect x="3" y="6" width="18" height="12"/><path d="M3 6l9 7 9-7"/></svg></span><span class="contact__text">your.email@yoursite.com</span></li>
      <li class="contact__row"><span class="contact__icon"><svg viewBox="0 0 24 24"><circle cx="12" cy="12" r="9"/><path d="M3 12h18M12 3c3 3 3 15 0 18M12 3c-3 3-3 15 0 18"/></svg></span><span class="contact__text">www.yoursite.com</span></li>
    </ul>
  </section>

</main>
</body>
</html>
```